Pool business needs attractive flyer

I just started my own pool service business, Here is the Information I want on the flyer but you put it anyway you think best.

Service Call $45
which Includes: Chemical Balance, Inspect all equipment, Skim water surface, clean filters.

Vacuum $10
Please Call, txt or Email for chemical price list

Other Services Include:
Supply and install Pumps, Chlorinators, Automatic Cleaners & Spare Parts

My Name
0438215967
TidesMail@vorlix.com

Pool Service

```html
<!DOCTYPE html>
<html lang="en">
<head>
<meta charset="utf-8">
<title>Clearwave Pool Care – Flyer</title>
<link rel="stylesheet" href="https://fonts.googleapis.com/css2?family=Open+Sans:wght@400;700;800&display=swap">
<style>
  :root {
    --sky-white: #ffffff;
    --pool-blue: #0aa4e4;
    --deep-blue: #1c5cb4;
    --brand-blue: #1f3f9c;
    --panel-blue: #8fc6ee;
    --panel-text: #123a6e;
    --wave-light: #b9e3f7;
    --footer-navy: #0c1552;
    --footer-name: #a9d6f6;
    --footer-text: #8cc8f2;
    --text-white: #ffffff;
  }
  * { box-sizing: border-box; margin: 0; padding: 0; }
  html, body { width: 851px; height: 1200px; overflow: hidden; }
  body { font-family: "Open Sans", sans-serif; }

  .flyer {
    position: relative;
    width: 851px;
    height: 1200px;
    overflow: hidden;
    background: linear-gradient(180deg,
      var(--sky-white) 0px,
      var(--sky-white) 330px,
      var(--pool-blue) 560px,
      #1387d6 760px,
      var(--deep-blue) 1000px);
  }

  .brand {
    position: absolute;
    top: 220px;
    left: 0;
    width: 851px;
    text-align: center;
    color: var(--brand-blue);
    font-weight: 800;
    line-height: 1;
  }
  .brand__line { display: block; }
  .brand__line--top { font-size: 104px; letter-spacing: 1px; }
  .brand__line--bottom { font-size: 118px; letter-spacing: 2px; margin-top: 14px; }

  .offer {
    position: absolute;
    left: 0;
    width: 851px;
    text-align: center;
    color: var(--text-white);
  }
  .offer__title { font-weight: 700; font-size: 34px; line-height: 1.2; }
  .offer__detail { font-weight: 400; font-size: 26px; line-height: 1.42; }
  .offer--service { top: 556px; }
  .offer--vacuum { top: 713px; }

  .services-panel {
    position: absolute;
    left: 136px;
    top: 857px;
    width: 582px;
    height: 150px;
    border-radius: 18px;
    background: var(--panel-blue);
    border: 3px solid #ffffff;
    box-shadow: 0 0 14px rgba(255,255,255,0.9);
    text-align: center;
    color: var(--panel-text);
    padding-top: 18px;
  }
  .services-panel__title { font-weight: 700; font-size: 25px; line-height: 1.3; }
  .services-panel__list { font-weight: 400; font-size: 22px; line-height: 1.45; }

  .waves {
    position: absolute;
    left: 0;
    top: 960px;
    width: 851px;
    height: 240px;
  }

  .contact {
    position: absolute;
    left: 0;
    top: 1090px;
    width: 851px;
    height: 110px;
  }
  .contact__name {
    text-align: center;
    font-weight: 700;
    font-size: 34px;
    color: var(--footer-name);
    line-height: 1;
  }
  .contact__phone, .contact__email {
    position: absolute;
    top: 52px;
    font-size: 24px;
    color: var(--footer-text);
    line-height: 1;
  }
  .contact__phone { left: 33px; }
  .contact__email { right: 30px; }
</style>
</head>
<body>
<main class="flyer">
  <h1 class="brand">
    <span class="brand__line brand__line--top">Clearwave</span>
    <span class="brand__line brand__line--bottom">POOL CARE</span>
  </h1>

  <section class="offer offer--service">
    <h2 class="offer__title">Service Call $45</h2>
    <p class="offer__detail">Includes: Chemical Balance, Inspect all equipment,<br>Skim water surface, clean filters.</p>
  </section>

  <section class="offer offer--vacuum">
    <h2 class="offer__title">Vacuum $10</h2>
    <p class="offer__detail">Please Call, txt or Email for chemical price list</p>
  </section>

  <section class="services-panel">
    <h3 class="services-panel__title">Other Services Include:</h3>
    <p class="services-panel__list">Supply and install Pumps, Chlorinators,<br>Automatic Cleaners &amp; Spare Parts</p>
  </section>

  <svg class="waves" viewBox="0 0 851 240" aria-hidden="true">
    <path d="M0 60 C140 10 260 0 420 40 C560 75 700 50 851 0 L851 240 L0 240 Z" fill="#ffffff"/>
    <path d="M0 75 C150 35 270 30 420 62 C570 94 710 80 851 30 L851 240 L0 240 Z" fill="var(--wave-light)"/>
    <path d="M0 88 C150 55 280 50 430 80 C580 110 720 100 851 62 L851 240 L0 240 Z" fill="#ffffff"/>
    <path d="M0 110 C160 90 300 90 450 105 C600 120 740 110 851 95 L851 240 L0 240 Z" fill="var(--footer-navy)"/>
  </svg>

  <footer class="contact">
    <p class="contact__name">NAME GOES HERE</p>
    <p class="contact__phone">0438215967</p>
    <p class="contact__email">TidesMail@vorlix.com</p>
  </footer>
</main>
</body>
</html>
```